tilebaron.org needs a cool website!

I need a website designed for a commercial flooring maintenance company based in Texas. We will be providing services like carpet shampooing, burnishing, resurfacing and power washing. It needs to be cool and trendy.

I’ll need 10-20 pages. I need help deciding on the style and color palette. We will need great stock pictures of different flooring types and you will need to photo shop our logo on imaginary cars or storefronts.

Please have similar experience and an open mind. I’m looking for a partnership and someone to turn to for future projects and upkeep.

The domain is currently hosted on Wix. You will need the ability to develop and code it there.
Updates

Target Market(s)

Commercial businesses and properties

Industry/Entity Type

Floor care

Coding

Coded - Design and coding required

Number of Pages Required

5+ page

Requirements
Must have
• Great pictures of different types of floors.

```html
<!DOCTYPE html>
<html lang="en">
<head>
<meta charset="utf-8">
<title>Tilebaron – Professional Flooring Maintenance</title>
<link rel="stylesheet" href="https://fonts.googleapis.com/css2?family=Poppins:wght@400;500;600;700;800&display=swap">
<style>
:root{
  --green:#8dc63f;
  --green-dark:#6fa52a;
  --ink:#151515;
  --text:#6b6b6b;
  --light:#f1f1f1;
  --field:#ebe9ea;
  --white:#ffffff;
  --footer:#101010;
}
*{box-sizing:border-box;margin:0;padding:0}
html,body{width:1200px;height:5199px;overflow:hidden}
body{font-family:"Poppins",sans-serif;color:var(--ink);background:var(--white);position:relative}
section,header,footer{position:absolute;left:0;width:1200px;overflow:hidden}
.abs{position:absolute}
.photo{position:absolute;border-radius:50%;overflow:hidden;box-shadow:inset 0 0 40px rgba(0,0,0,.18)}
.btn{position:absolute;background:var(--green);color:var(--white);font-weight:600;font-size:14px;border-radius:6px;display:flex;align-items:center;justify-content:center}
.eyebrow{color:var(--green);font-size:13px;font-weight:500}
.h2{font-size:36px;font-weight:700;line-height:1.25;color:var(--ink)}
.center{left:0;width:1200px;text-align:center}
.body-text{font-size:13px;line-height:22px;color:var(--text)}

/* hero */
.hero{top:0;height:742px;background:#2e2d2b}
.hero-scene{inset:0;background:
  radial-gradient(ellipse 420px 300px at 420px 200px,rgba(150,140,125,.35),transparent 70%),
  radial-gradient(ellipse 600px 200px at 500px 700px,rgba(90,85,78,.6),transparent 70%),
  linear-gradient(100deg,#1f1f1f 0%,#33312e 40%,#4b4843 75%,#2b2a28 100%)}
.brand{font-size:34px;font-weight:500;color:var(--white);display:flex;align-items:center;gap:10px}
.brand-dot{width:14px;height:14px;border-radius:50%;background:var(--green)}
.nav{position:absolute;top:48px;left:452px;display:flex;gap:38px;font-size:13px;font-weight:500;color:var(--white)}
.nav-cta{position:absolute;left:970px;top:37px;width:142px;height:42px;border:2px solid var(--white);border-radius:6px;color:var(--white);font-size:14px;font-weight:500;display:flex;align-items:center;justify-content:center}
.hero-title{left:88px;top:232px;font-size:52px;font-weight:800;line-height:58px;color:var(--white)}
.hero-text{left:88px;top:436px;width:490px;font-size:13px;line-height:24px;color:#e6e6e6}
.play{position:absolute;left:284px;top:514px;width:42px;height:42px;border-radius:50%;background:var(--green);display:flex;align-items:center;justify-content:center}
.play-label{left:337px;top:524px;color:var(--white);font-size:14px;font-weight:500}
.ring{border:3px solid var(--white)}

/* how */
.how{top:742px;height:503px;background:var(--green)}
.how-title{top:50px;left:0;width:1200px;display:flex;align-items:center;justify-content:center;gap:28px;font-size:30px;font-weight:700}
.how-title span.line{width:380px;height:1px;background:rgba(0,0,0,.45)}
.step{position:absolute;top:133px;width:312px;height:312px;border-radius:50%;background:var(--white);text-align:center}
.step-icon{width:100px;height:100px;border-radius:50%;margin:30px auto 0;border:2px solid #ddd;display:flex;align-items:center;justify-content:center;background:#f6f6f6}
.step-icon.active{background:var(--green);border-color:var(--green)}
.step h3{font-size:19px;font-weight:700;margin-top:28px}
.step p{font-size:13px;line-height:22px;color:var(--text);width:250px;margin:12px auto 0}
.step .arrow{position:absolute;left:131px;top:280px;width:50px;height:50px;border-radius:50%;background:var(--ink);display:flex;align-items:center;justify-content:center}

/* about */
.about{top:1245px;height:635px}
.badge{position:absolute;border-radius:50%;background:var(--white);border:5px solid var(--green);display:flex;align-items:center;justify-content:center}
.badge-mark{width:46px;height:46px;border-radius:50%;background:var(--ink)}

/* services */
.services{top:1880px;height:698px;background:var(--light)}
.svc{position:absolute;top:210px;width:300px;height:300px;border-radius:50%;background:var(--white);box-shadow:0 12px 28px rgba(0,0,0,.08)}
.svc .ring-green{position:absolute;left:75px;top:75px;width:150px;height:150px;border-radius:50%;background:var(--green);box-shadow:8px 10px 18px rgba(0,0,0,.18);display:flex;align-items:center;justify-content:center}
.svc .ring-in{width:118px;height:118px;border-radius:50%;background:var(--white);display:flex;align-items:center;justify-content:center}
.svc-label{position:absolute;top:540px;width:300px;text-align:center;font-size:19px;font-weight:600}

/* why */
.why{top:2578px;height:720px;background:#fafafa}
.ticks{left:88px;top:320px;list-style:none;font-size:14px;font-weight:500;color:#333;line-height:25px}
.ticks li{display:flex;align-items:center;gap:10px}
.ticks li::before{content:"";width:9px;height:9px;border-radius:50%;background:var(--green)}

/* gallery */
.gallery{top:3298px;height:696px;background:var(--light)}
.dots{top:640px;left:572px;display:flex;gap:6px}
.dots i{width:14px;height:14px;border-radius:50%;background:#8a8a8a}
.dots i.on{background:var(--green)}

/* contact */
.contact{top:3994px;height:656px}
.field{position:absolute;background:var(--field);border-radius:6px;font-size:12px;color:#333;padding:20px 26px;height:56px}

/* cta */
.cta{top:4650px;height:205px;background:var(--green)}
.cta-circle{position:absolute;left:924px;top:32px;width:144px;height:144px;border-radius:50%;background:var(--white);display:flex;flex-direction:column;align-items:center;justify-content:center;gap:10px;font-size:14px;font-weight:500}

/* footer */
.footer{top:4855px;height:344px;background:var(--footer);color:var(--white)}
.foot-h{font-size:24px;font-weight:600}
.foot-links{list-style:none;font-size:12px;line-height:27px}
.contact-row{display:flex;gap:10px;font-size:12px;line-height:16px;margin-bottom:14px}
.social{position:absolute;top:104px;width:46px;height:46px;border-radius:50%;background:#2a2a2a;border:1px solid #555}
.social.on{background:var(--green);border-color:var(--green)}
.foot-rule{left:88px;top:282px;width:1024px;height:1px;background:#333}
.copyright{top:300px;left:0;width:1200px;text-align:center;font-size:12px;color:#ddd}
.chat{position:absolute;left:1125px;top:272px;width:48px;height:44px;border-radius:50%;background:var(--green)}
</style>
</head>
<body>

<header class="hero">
  <div role="img" aria-label="Cleaner vacuuming a living room floor" class="abs hero-scene"></div>
  <div class="abs brand" style="left:88px;top:32px"><span>tilebaron</span><span class="brand-dot"></span></div>
  <nav class="nav"><span>Home</span><span>Introduction</span><span>Services</span><span>Why Choose</span><span>Paragraph</span></nav>
  <div class="nav-cta">Contact Us</div>

  <h1 class="abs hero-title">Welcome To<br>Professional Flooring<br>Maintenance</h1>
  <p class="abs hero-text">Expert care for your floors – from carpet shampooing to power washing, we keep your spaces spotless and shining.</p>
  <div class="btn" style="left:88px;top:514px;width:178px;height:42px">Book Appointment</div>
  <div class="play"><svg width="14" height="14" viewBox="0 0 14 14"><circle cx="7" cy="7" r="7" fill="#fff"/><path d="M5.5 4.2 9.8 7 5.5 9.8Z" fill="#8dc63f"/></svg></div>
  <span class="abs play-label">How We Works</span>

  <div class="photo ring" role="img" aria-label="Cleaner scrubbing a black and white checkered tile floor" style="left:663px;top:222px;width:180px;height:180px;background:radial-gradient(circle at 60% 30%,#f2f0ec 0%,#cfcbc5 30%,transparent 55%),linear-gradient(150deg,#ece9e4 0%,#2a2a2a 45%,#e6e3de 62%,#1f1f1f 100%)"></div>
  <div class="photo ring" role="img" aria-label="Cleaner vacuuming a rug beside a grey sofa" style="left:870px;top:180px;width:300px;height:300px;background:radial-gradient(circle at 62% 38%,#3d4d62 0%,#56657a 12%,transparent 26%),radial-gradient(ellipse 130px 60px at 40% 55%,#b8bcbf,transparent 70%),linear-gradient(180deg,#f4f3f0 0%,#e4e3df 45%,#c9c6c0 75%,#a9a49c 100%)"></div>
  <div class="photo ring" role="img" aria-label="Worker kneeling to polish a bright white floor" style="left:700px;top:435px;width:262px;height:262px;background:radial-gradient(circle at 55% 35%,#2f4a6e 0%,#3c5a82 12%,transparent 24%),linear-gradient(180deg,#b9b8b4 0%,#d6d4cf 45%,#f3f2ee 70%,#fbfaf7 100%)"></div>
  <div class="abs" style="left:1062px;top:431px;width:72px;height:72px;border-radius:50%;background:var(--green);border:4px solid #fff;display:flex;align-items:center;justify-content:center">
    <svg width="26" height="24" viewBox="0 0 26 24"><path d="M13 23 2.5 12.5A6.5 6.5 0 0 1 13 4.5a6.5 6.5 0 0 1 10.5 8Z" fill="#fff"/></svg>
  </div>
</header>

<section class="how">
  <div class="abs how-title"><span class="line"></span><span>How It Works</span><span class="line"></span></div>

  <div class="step" style="left:111px">
    <div class="step-icon"><svg width="46" height="46" viewBox="0 0 46 46" fill="none" stroke="#8dc63f" stroke-width="2.5"><rect x="5" y="9" width="30" height="28" rx="3"/><path d="M5 17h30M13 5v8M27 5v8"/><circle cx="33" cy="33" r="9" fill="#f6f6f6"/><path d="M33 28v5l3 2"/></svg></div>
    <h3>Book A Date</h3>
    <p>Easily book in minutes 100% online with a confirmed available timeslot</p>
    <div class="arrow"><svg width="16" height="16" viewBox="0 0 16 16" stroke="#fff" stroke-width="2" fill="none"><path d="M3 13 13 3M5 3h8v8"/></svg></div>
  </div>
  <div class="step" style="left:444px">
    <div class="step-icon active"><svg width="46" height="46" viewBox="0 0 46 46" fill="#fff"><rect x="6" y="6" width="34" height="20" rx="4"/><circle cx="15" cy="16" r="3" fill="#8dc63f"/><circle cx="23" cy="16" r="3" fill="#8dc63f"/><circle cx="31" cy="16" r="3" fill="#8dc63f"/><circle cx="23" cy="31" r="4"/><path d="M15 42a8 8 0 0 1 16 0Z"/></svg></div>
    <h3>Manage Online</h3>
    <p>Check your status, make changes, and view progress of the cleaner online or in the app</p>
    <div class="arrow"><svg width="16" height="16" viewBox="0 0 16 16" stroke="#fff" stroke-width="2" fill="none"><path d="M3 13 13 3M5 3h8v8"/></svg></div>
  </div>
  <div class="step" style="left:777px">
    <div class="step-icon"><svg width="46" height="46" viewBox="0 0 46 46" fill="none" stroke="#8dc63f" stroke-width="2.5"><circle cx="22" cy="11" r="4"/><path d="M8 36h26l4-8M14 20l8 6 8-4M10 26l6 6"/></svg></div>
    <h3>Site Back &amp; Relax</h3>
    <p>As we know your home better, we are able to improve the xperience for even</p>
    <div class="arrow"><svg width="16" height="16" viewBox="0 0 16 16" stroke="#fff" stroke-width="2" fill="none"><path d="M3 13 13 3M5 3h8v8"/></svg></div>
  </div>
</section>

<section class="about">
  <div class="abs" style="left:141px;top:86px;width:432px;height:432px;border-radius:50%;border:1px solid #555"></div>
  <div class="photo" role="img" aria-label="Technician in black gloves installing beige floor tiles" style="left:148px;top:94px;width:418px;height:418px;background:radial-gradient(ellipse 120px 150px at 48% 40%,#1e1e1e 0%,#2c2c2c 55%,transparent 75%),radial-gradient(circle at 60% 18%,#f5f5f3 0%,transparent 22%),linear-gradient(180deg,#e6e3dd 0%,#cfc9c0 40%,#bfb5a4 70%,#a3998a 100%)"></div>
  <div class="badge" style="left:146px;top:417px;width:126px;height:126px"><span class="badge-mark"></span></div>
  <p class="abs eyebrow" style="left:613px;top:186px">About Us</p>
  <h2 class="abs h2" style="left:613px;top:208px;font-size:38px">Tilebaron Introduction</h2>
  <p class="abs body-text" style="left:613px;top:272px;width:440px">Welcome to [Tilebaron], Texas' trusted flooring maintenance specialists. We provide top-quality services like carpet shampooing, burnishing, resurfacing, and power washing, ensuring your commercial spaces always look their best. With a focus on professionalism and efficiency, we deliver results you can rely on.</p>
  <div class="btn" style="left:613px;top:433px;width:130px;height:40px">Read More</div>
</section>

<section class="services">
  <p class="abs eyebrow center" style="top:60px">Our Services</p>
  <h2 class="abs h2 center" style="top:88px">Services We Offered On<br>Tilebaron</h2>

  <div class="svc" style="left:88px"><div class="ring-green"><div class="ring-in"><svg width="60" height="60" viewBox="0 0 60 60"><circle cx="18" cy="14" r="5"/><path d="M12 22h10l2 14h-4l-1 14h-4l-1-14h-4Z"/><path d="M28 30l14-8 12 16-14 8Z" fill="#222"/></svg></div></div></div>
  <div class="svc" style="left:328px"><div class="ring-green"><div class="ring-in"><svg width="60" height="60" viewBox="0 0 60 60"><rect x="16" y="26" width="30" height="16" rx="3"/><rect x="22" y="10" width="6" height="16"/><rect x="34" y="14" width="6" height="12"/><circle cx="20" cy="46" r="4"/><circle cx="42" cy="46" r="4"/><path d="M8 52h44" stroke="#000" stroke-width="2"/></svg></div></div></div>
  <div class="svc" style="left:568px"><div class="ring-green"><div class="ring-in"><svg width="60" height="60" viewBox="0 0 60 60"><path d="M30 16h12l6 10v24H28V26Z"/><rect x="34" y="34" width="8" height="10" fill="#fff"/><path d="M14 16v30" stroke="#000" stroke-width="3"/><path d="M10 8h10" stroke="#000" stroke-width="2" stroke-dasharray="2 2"/><rect x="10" y="44" width="8" height="6"/></svg></div></div></div>
  <div class="svc" style="left:808px"><div class="ring-green"><div class="ring-in"><svg width="60" height="60" viewBox="0 0 60 60"><circle cx="28" cy="30" r="20"/><path d="M18 24h8M30 34h10M20 38h6" stroke="#fff" stroke-width="3"/><circle cx="44" cy="44" r="7" fill="#fff" stroke="#000" stroke-width="2"/><path d="M44 40v8M40 44h8" stroke="#000" stroke-width="2"/></svg></div></div></div>

  <p class="svc-label" style="left:88px">Carpet Shampooing</p>
  <p class="svc-label" style="left:328px">Burnishing</p>
  <p class="svc-label" style="left:568px">Power Washing</p>
  <p class="svc-label" style="left:808px">Resurfacing</p>

  <div class="btn" style="left:515px;top:618px;width:170px;height:40px">View All Services</div>
</section>

<section class="why">
  <h2 class="abs h2" style="left:88px;top:212px">Tilebaron Why<br>Choose Us</h2>
  <ul class="abs ticks">
    <li>State-of-the-art equipment and techniques</li>
    <li>Reliable, professional service</li>
    <li>Tailored solutions for commercial properties</li>
    <li>Dedicated to delivering pristine results every time</li>
  </ul>
  <div class="btn" style="left:88px;top:442px;width:128px;height:40px">Read More</div>

  <div class="abs" style="left:617px;top:90px;width:490px;height:490px;border-radius:50%;border:1px solid #555"></div>
  <div class="photo" role="img" aria-label="Company storefront with glass doors and window posters" style="left:632px;top:105px;width:460px;height:460px;background:radial-gradient(ellipse 60px 50px at 32% 62%,#3f6fb0,transparent 70%),radial-gradient(ellipse 50px 70px at 68% 64%,#c9c7c2,transparent 70%),linear-gradient(180deg,#dfe1e2 0%,#cfd1d2 32%,#4a4e52 40%,#23272b 58%,#3a3e42 72%,#8e8d89 80%,#b3b1ac 100%)"></div>
  <div class="abs" style="left:743px;top:150px;font-size:40px;font-weight:500;color:#222">tilebaron</div>
  <div class="badge" style="left:873px;top:444px;width:146px;height:146px;border:none;box-shadow:0 6px 18px rgba(0,0,0,.15)"><span class="badge-mark" style="width:56px;height:56px"></span></div>
</section>

<section class="gallery">
  <p class="abs eyebrow center" style="top:68px">Our Gallery</p>
  <h2 class="abs h2 center" style="top:96px">Gallery We Offered On<br>Tilebaron</h2>
  <div class="photo" role="img" aria-label="Worker cutting flooring with a blue power tool" style="left:-28px;top:300px;width:216px;height:216px;background:radial-gradient(circle at 55% 40%,#3a6fa8 0%,transparent 30%),linear-gradient(170deg,#8fa0ac 0%,#6a6258 45%,#c79a5c 75%,#9c7040 100%)"></div>
  <div class="photo" role="img" aria-label="Installer laying wooden floor planks" style="left:187px;top:300px;width:216px;height:216px;background:radial-gradient(circle at 50% 35%,#3c3c3c 0%,transparent 30%),linear-gradient(180deg,#e2ddd6 0%,#cfc6bb 40%,#9b6842 65%,#7a4a2a 100%)"></div>
  <div class="photo" role="img" aria-label="Worker in yellow hard hat leveling a tile floor" style="left:413px;top:222px;width:370px;height:370px;background:radial-gradient(circle at 50% 18%,#e3b62c 0%,#e3b62c 8%,transparent 14%),radial-gradient(ellipse 110px 90px at 50% 42%,#a8a39a,transparent 70%),linear-gradient(180deg,#d6cdb9 0%,#bdb29b 35%,#8f8d88 60%,#b4b2ad 80%,#6f6e6a 100%)"></div>
  <div class="photo" role="img" aria-label="Hands fitting grey laminate boards" style="left:797px;top:300px;width:216px;height:216px;background:linear-gradient(135deg,#d7d5d1 0%,#a9a7a3 40%,#7c7a77 70%,#5d5c5a 100%)"></div>
  <div class="photo" role="img" aria-label="Installer fitting hardwood flooring" style="left:1028px;top:300px;width:216px;height:216px;background:radial-gradient(circle at 55% 30%,#8a8a8a 0%,transparent 28%),linear-gradient(180deg,#e3dcd2 0%,#c9a888 45%,#a06a3e 75%,#7a4c28 100%)"></div>
  <div class="abs dots"><i></i><i class="on"></i><i></i></div>
</section>

<section class="contact">
  <h2 class="abs center" style="top:98px;font-size:32px;font-weight:700">Get In Touch With Us</h2>
  <p class="abs center" style="top:146px;font-size:11.5px;line-height:20px;color:var(--text)">Have questions about our services or need a quote for your flooring maintenance needs? Our team is<br>ready to assist you. Simply fill out the form below, and we'll get back to you as soon as possible.</p>
  <div class="field" style="left:222px;top:228px;width:370px">First Name</div>
  <div class="field" style="left:606px;top:228px;width:370px">Last Name</div>
  <div class="field" style="left:222px;top:301px;width:370px">E mail</div>
  <div class="field" style="left:606px;top:301px;width:370px">Phone</div>
  <div class="field" style="left:222px;top:374px;width:754px;height:124px">How Can We Help You ?</div>
  <div class="btn" style="left:530px;top:514px;width:140px;height:40px;border-radius:20px">Submit</div>
</section>

<section class="cta">
  <h2 class="abs" style="left:132px;top:60px;font-size:33px;font-weight:700">Ready to transform your floors?</h2>
  <p class="abs" style="left:132px;top:114px;width:460px;font-size:13px;line-height:20px;color:#1c2a0c">Contact us today for a free consultation! Let's work together to keep your commercial space looking its best.</p>
  <div class="cta-circle"><svg width="26" height="26" viewBox="0 0 26 26" stroke="#111" stroke-width="2" fill="none"><path d="M5 21 21 5M9 5h12v12"/></svg><span>Contact Us</span></div>
</section>

<footer class="footer">
  <div class="abs brand" style="left:88px;top:128px;font-size:40px"><span>tilebaron</span><span class="brand-dot"></span></div>

  <h3 class="abs foot-h" style="left:403px;top:40px">Quick link</h3>
  <ul class="abs foot-links" style="left:403px;top:84px">
    <li>Home</li><li>Introduction</li><li>Services</li><li>Why Choose</li><li>Paragraph</li><li>Contact</li>
  </ul>

  <h3 class="abs foot-h" style="left:630px;top:40px">Contact us</h3>
  <div class="abs" style="left:630px;top:88px">
    <div class="contact-row"><svg width="12" height="12" viewBox="0 0 12 12"><path d="M2 1h3l1 3-2 1a7 7 0 0 0 3 3l1-2 3 1v3c-6 0-10-4-10-10Z" fill="#8dc63f"/></svg><div>Phone<br>(123) 456-7890</div></div>
    <div class="contact-row"><svg width="12" height="12" viewBox="0 0 12 12"><rect x="0" y="2" width="12" height="8" fill="#8dc63f"/><path d="M0 2 6 7l6-5" stroke="#101010" fill="none"/></svg><div>Email<br>info@tilebaron.org</div></div>
    <div class="contact-row"><svg width="12" height="14" viewBox="0 0 12 14"><path d="M6 14S1 8 1 5a5 5 0 0 1 10 0c0 3-5 9-5 9Z" fill="#8dc63f"/><circle cx="6" cy="5" r="2" fill="#101010"/></svg><div>Address<br>123 Steelworks Lane, City, State, ZIP</div></div>
  </div>

  <h3 class="abs foot-h" style="left:922px;top:40px">Follow us</h3>
  <span class="social on" style="left:924px"></span>
  <span class="social" style="left:979px"></span>
  <span class="social" style="left:1032px"></span>

  <div class="abs foot-rule"></div>
  <p class="abs copyright">© Copyrights 2024, Tilebaron, All Rights Reserved</p>
  <span class="chat"></span>
</footer>

</body>
</html>
```